Corvid Lens Studio Business Card Design

I need a business card designed for a photography business based in Perth, Western Australia called Corvid Lens Studio.

We specialise in wedding, event photography and portrait photography.

The business card must borrow the style of the attached logo.

The hex codes for the colours in the logo are:
#ED1D85 - Pink
#89C23E - Green
#37282F - Black

The name on the card will be:
Name: Tobiah
Phone: 0417395268
Website: www.corvidlensstudio.com.au
Facebook: corvidlensstudio

I am open and happy to accept creative concepts.

Industry/Entity Type

Business

```html
<!DOCTYPE html>
<html lang="en">
<head>
<meta charset="utf-8">
<title>Corvid Lens Studio – Business Card</title>
<link rel="stylesheet" href="https://fonts.googleapis.com/css2?family=Jost:wght@400&family=Marcellus&family=EB+Garamond:ital@1&display=swap">
<style>
  :root {
    --pink: #ED1D85;
    --green: #89C23E;
    --ink: #37282F;
    --card-dark: #201823;
    --trim: #8FE3EE;
    --paper: #FFFFFF;
    --text-light: #F4F1F5;
  }
  * { margin: 0; padding: 0; box-sizing: border-box; }
  html, body {
    width: 1000px;
    height: 1200px;
    overflow: hidden;
    background: var(--paper);
  }
  .sheet {
    position: relative;
    width: 1000px;
    height: 1200px;
  }
  .card {
    position: absolute;
    border: 1px solid var(--trim);
  }

  /* Front */
  .card--front {
    left: 139px; top: 67px;
    width: 725px; height: 438px;
    background: var(--paper);
  }
  .brand-dot {
    position: absolute;
    left: 290px; top: 146px;
    width: 144px; height: 144px;
    border-radius: 50%;
    background: var(--pink);
  }
  .brand-name {
    position: absolute;
    left: 0; right: 0; top: 336px;
    text-align: center;
    font-family: "Jost", sans-serif;
    font-weight: 400;
    font-size: 22px;
    letter-spacing: 0.9em;
    padding-left: 0.9em;
    color: var(--ink);
    text-transform: uppercase;
  }

  /* Back */
  .card--back {
    left: 140px; top: 684px;
    width: 727px; height: 437px;
    background: var(--card-dark);
  }
  .services {
    position: absolute;
    left: 55px; top: 120px;
    list-style: none;
    font-family: "Marcellus", serif;
    font-size: 24px;
    line-height: 28.5px;
    color: var(--text-light);
    text-transform: uppercase;
    letter-spacing: 0.02em;
  }
  .services li {
    display: flex;
    align-items: center;
  }
  .services .marker {
    width: 8px; height: 8px;
    margin-right: 5px;
    margin-top: -10px;
    flex: none;
  }
  .services .trail {
    margin-left: 4px;
    margin-top: -2px;
  }
  .contact {
    position: absolute;
    left: 65px; top: 304px;
    font-family: "EB Garamond", serif;
    font-style: italic;
    font-size: 17px;
    line-height: 24.5px;
    color: var(--text-light);
  }
  .brand-discs {
    position: absolute;
    left: 586px; top: 6px;
    width: 132px;
    height: 426px;
  }
</style>
</head>
<body>
<main class="sheet">

  <section class="card card--front" aria-label="Card front">
    <div class="brand-dot" aria-hidden="true"></div>
    <h1 class="brand-name">Corvid Lens Studio</h1>
  </section>

  <section class="card card--back" aria-label="Card back">
    <ul class="services">
      <li>
        <svg class="marker" viewBox="0 0 8 8" aria-hidden="true"><polygon points="0,0 8,0 2,8" fill="var(--green)"/></svg>
        Wedding
      </li>
      <li>
        <svg class="marker" viewBox="0 0 8 8" aria-hidden="true"><polygon points="0,0 8,0 2,8" fill="var(--pink)"/></svg>
        Event Photography
      </li>
      <li>
        <svg class="marker" viewBox="0 0 8 8" aria-hidden="true"><polygon points="0,0 8,0 2,8" fill="var(--text-light)"/></svg>
        Portrait Photography
        <svg class="trail" width="28" height="8" viewBox="0 0 28 8" aria-hidden="true">
          <polygon points="0,0 6,0 1.5,6" fill="var(--text-light)"/>
          <polygon points="10,0 16,0 11.5,6" fill="var(--text-light)"/>
          <polygon points="20,0 26,0 21.5,6" fill="var(--text-light)"/>
        </svg>
      </li>
    </ul>

    <address class="contact">
      Tobiah<br>
      Phone: 0417395268<br>
      Website: www.corvidlensstudio.com.au<br>
      Facebook: corvidlensstudio
    </address>

    <svg class="brand-discs" viewBox="0 0 132 426" aria-hidden="true">
      <circle cx="66" cy="68" r="64" fill="var(--green)"/>
      <circle cx="66" cy="210" r="64" fill="var(--pink)"/>
      <circle cx="66" cy="356" r="64" fill="var(--text-light)"/>
    </svg>
  </section>

</main>
</body>
</html>
```